BrimKettle international mobile topups web site | ||
Cell phone topup and billing services | ||
Information Technology | ||
www.brimkettle-demo.net | ||
BrimKettle provides payment services and mobile account topups connected to a number of mobile operators. The company facilitates people from developed countries to topup phones of their relatives in developing countries. | ||
The site expresses strong unique image which is consistent with corporate branding and logo (see uploaded files). The design should inspire action, trust, value and intuitiveness for clients. |
Cutting-Edge Unique/Creative Professional Trendy Friendly International Corporate Inspirational Progressive Service Oriented High Tech |
Green (as in logo) | ||
Blue (as in logo) | ||
Shades of Gray | ||
top | ||
www.vandroplex-demo.net | ||
www.korvaset-demo.ru | ||
www.tullwenberg-demo.net | ||

```html
<!DOCTYPE html>
<html lang="en">
<head>
<meta charset="utf-8">
<title>BrimKettle – International Mobile Topups</title>
<link href="https://fonts.googleapis.com/css2?family=PT+Sans:wght@400;700&display=swap" rel="stylesheet">
<style>
:root{
  --blue-deep:#123f9e;
  --blue:#1f5fc8;
  --blue-light:#6fa6ea;
  --blue-pale:#dce9f9;
  --green:#6cbf2a;
  --green-dark:#4c9a17;
  --green-light:#a4dc5c;
  --ink:#1d3f8f;
  --text:#555b66;
  --grey:#e9ecef;
  --grey-line:#c9ced6;
  --nav:#222428;
  --night:#0c0d10;
  --white:#ffffff;
  --op-red:#d8232a;
  --op-magenta:#d3177a;
  --op-navy:#1f3a8a;
  --op-cyan:#1d8fd0;
  --op-grey:#444a55;
}
*{box-sizing:border-box;margin:0;padding:0}
html,body{width:1200px;height:939px;overflow:hidden}
body{position:relative;background:var(--white);font-family:"PT Sans",Arial,sans-serif;color:var(--text)}

.header-bg{position:absolute;left:0;top:0;width:1200px;height:400px;
  background:radial-gradient(ellipse at 50% 55%,var(--blue-light) 0%,var(--blue) 45%,var(--blue-deep) 100%)}
.header-band{position:absolute;left:0;top:378px;width:1200px;height:24px;
  background:linear-gradient(var(--blue),var(--blue-deep))}
.page-glow{position:absolute;left:0;top:402px;width:1200px;height:448px;
  background:linear-gradient(var(--blue-pale),var(--white) 45%)}
.night{position:absolute;left:0;top:850px;width:1200px;height:89px;background:var(--night)}

.masthead{position:absolute;left:127px;top:0;width:940px;height:356px;
  background:linear-gradient(#fff 0%,#f3f6fa 70%,#dfe7f2 100%);border-radius:0 0 40px 40px}
.login{position:absolute;top:5px;right:18px;display:flex;gap:8px;align-items:center;font-size:11px;color:var(--ink);font-weight:700}
.login .field{width:92px;height:14px;background:var(--blue-light);border-radius:2px}
.login .go{width:32px;height:14px;background:var(--green);border-radius:2px;font-size:9px;color:var(--white);text-align:center;line-height:14px}

.brand{position:absolute;left:50px;top:72px;display:flex;align-items:center;gap:12px}
.brand-mark{width:56px;height:56px;border-radius:50%;background:var(--blue)}
.brand-name{font-size:40px;font-weight:700;color:var(--blue-deep);line-height:1}
.brand-tag{position:absolute;left:118px;top:118px;font-size:15px;color:var(--green-dark)}

.nav{position:absolute;left:335px;top:81px;width:598px;height:46px;background:linear-gradient(#3b3e44,var(--nav));
  border-radius:6px;display:flex}
.nav a{flex:1;color:var(--white);text-decoration:none;font-size:14px;line-height:16px;text-align:center;
  display:flex;align-items:center;justify-content:center;border-left:1px solid #4a4d54}
.nav a:first-child{border-left:0}

.hero-art{position:absolute;left:38px;top:148px;width:300px;height:208px;border-radius:50% 50% 0 0;
  background:radial-gradient(circle at 60% 45%,#eaf2fb,#a9c3e2 70%,#7f9fc8)}
.tagline{position:absolute;left:337px;top:244px;width:330px;font-size:19px;font-weight:700;line-height:22px;color:var(--ink)}
.pay-now{position:absolute;left:718px;top:241px;width:195px;height:70px;border-radius:4px;
  background:linear-gradient(var(--green-light),var(--green) 55%,var(--green-dark));
  color:var(--white);font-size:30px;display:flex;align-items:center;justify-content:center;gap:12px}

.content{position:absolute;left:140px;top:426px;width:920px;height:360px;background:var(--white)}
.intro{position:absolute;left:18px;top:20px;width:560px}
.intro h1{font-size:30px;color:var(--ink);font-weight:700;margin-bottom:14px;letter-spacing:-.2px}
.intro p{font-size:13.5px;line-height:18px;margin-bottom:14px}

.aside{position:absolute;left:608px;top:34px;width:290px}
.aside .tab{height:25px;line-height:25px;color:var(--white);font-size:13px;padding-left:12px;
  background:linear-gradient(var(--green-light),var(--green) 60%,var(--green-dark));
  clip-path:polygon(0 0,94% 0,100% 50%,94% 100%,0 100%)}
.aside p{font-size:12.5px;line-height:16px;padding:8px 12px 12px}
.aside .gap{height:28px}

.partners{position:absolute;left:17px;top:226px;width:883px}
.partner-tabs{display:flex;gap:8px;margin-left:22px;position:relative;top:2px}
.partner-tabs span{background:var(--white);border:2px solid var(--grey-line);border-bottom:0;border-radius:8px 8px 0 0;
  padding:3px 14px;font-size:15px;font-weight:700;color:var(--ink)}
.partner-strip{height:100px;border:2px solid var(--grey-line);border-radius:12px;background:linear-gradient(#fff,var(--grey));
  display:flex;align-items:center;justify-content:space-between;padding:0 18px}
.operator{font-size:19px;font-weight:700;color:var(--op-grey)}
.operator--red{color:var(--op-red)}
.operator--magenta{color:var(--op-magenta)}
.operator--navy{color:var(--op-navy)}
.operator--cyan{color:var(--op-cyan)}

.footer{position:absolute;left:140px;top:800px;width:920px;height:113px;border-radius:10px;
  background:linear-gradient(var(--blue),var(--blue-deep))}
.footer-links{position:absolute;left:36px;top:30px;font-size:13px;color:var(--white)}
.footer-links a{color:var(--white);text-decoration:none}
.footer-links i{font-style:normal;margin:0 6px}
.copy{position:absolute;left:36px;top:62px;font-size:13px;color:var(--white)}
.social{position:absolute;right:40px;top:34px;display:flex;gap:36px}
.social span{width:24px;height:24px;border-radius:50%;background:var(--blue-light)}
</style>
</head>
<body>
<div class="header-bg"></div>
<div class="header-band"></div>
<div class="page-glow"></div>
<div class="night"></div>

<header class="masthead">
  <div class="login">User Name: <span class="field"></span> Password: <span class="field"></span><span class="go">Go</span></div>
  <div class="brand"><span class="brand-mark"></span><span class="brand-name">BrimKettle</span></div>
  <div class="brand-tag">Global reach, local touch</div>
  <nav class="nav">
    <a href="#">Home</a><a href="#">About Us</a><a href="#">Our<br>Services</a><a href="#">Personal<br>Solutions</a><a href="#">Business<br>Solutions</a>
  </nav>
  <div class="hero-art" role="img" aria-label="Smartphone character holding a payment card in front of a globe"></div>
  <p class="tagline">Morbi dignissim bibendum elit, eu suscipit sapien placerat at. Vestibulum lacus purus, vestibulum at rhoncus.</p>
  <div class="pay-now">Pay Now <span>$</span></div>
</header>

<main class="content">
  <section class="intro">
    <h1>BrimKettle - International Mobile Topups</h1>
    <p>BrimKettle introduces an intuitive system designed to make it very easy for people to top up mobile phones and pay for utility bills, by providing them with an integrated online service accessible anytime, anywhere and on any device.</p>
    <p>The system delivers an easy set up of resellers of various levels and provides seamless integration to a wide variety of world-wide payment systems and Telco operators with a single façade.</p>
  </section>
  <aside class="aside">
    <div class="tab">Integration</div>
    <div class="gap"></div>
    <div class="tab">Global Reach</div>
    <p>BrimKettle provides Global Reach for customers having various needs in various countries worldwide</p>
    <div class="tab">Customer Experience</div>
  </aside>
  <section class="partners">
    <div class="partner-tabs"><span>Mobile Operators</span><span>Our Partners</span></div>
    <div class="partner-strip">
      <svg width="22" height="34" viewBox="0 0 22 34"><path d="M18 3 4 17l14 14" fill="none" stroke="#555b66" stroke-width="4"/></svg>
      <span class="operator operator--red">Vornaline</span>
      <span class="operator operator--navy">Telequista</span>
      <span class="operator operator--cyan">Tellmarq Group</span>
      <span class="operator operator--magenta">Tivomo</span>
      <span class="operator">Arlent</span>
      <span class="operator operator--red">Veridane Wireless</span>
      <svg width="22" height="34" viewBox="0 0 22 34"><path d="M4 3l14 14L4 31" fill="none" stroke="#555b66" stroke-width="4"/></svg>
    </div>
  </section>
</main>

<footer class="footer">
  <nav class="footer-links"><a href="#">Home</a><i>|</i><a href="#">About Us</a><i>|</i><a href="#">Our Services</a><i>|</i><a href="#">Personal Solutions</a><i>|</i><a href="#">Enterprise Solutions</a><i>|</i><a href="#">FAQ</a><i>|</i><a href="#">Contact Us</a></nav>
  <div class="copy">© 2011 BrimKettle. All Rights Reserved.</div>
  <div class="social" aria-label="Social links"><span></span><span></span><span></span></div>
</footer>
</body>
</html>
```